Verpackungen für Parfum-Proben
Besten Dank! Das Team ist begeistert - also bin ich es auch und wir freuen uns schon, unsere Parfum Proben in Zukunft in diesem tollen Design weitergeben zu können! Danke!
Zielgruppe
Hallo allerseits! Wir sind im Direktvertrieb in den Bereichen Parfum & Kosmetik tätig.
Aufgabenstellung
Für unsere Parfum-Proben benötige ich ein ansprechendes, modernes Design.
Das Design muss relativ neutral gehalten werden, da die Blister sowohl für Herren- als auch Damenproben verwendet werden.
Auf Vorder- und Rückseite soll unser Team-Logo (RuchKontor®) sichtbar sein (Vorderseite größer, Rückseite kleiner).
Auf der linken Innenseite sollte Plätz für einen netten Spruch (den ich mir noch überlege) sein.
Auf der Rückseite muss Platz (weißes / helles Feld) für einen Stempel und/oder Aufkleber (Kontaktdaten des Distributors) sein.
Unser Logo ist Lila - Das farbliche Design sollte dazu passen.
Bei Fragen, einfach Nachricht :)
Daten:
Endformat: 133 x 74 mm
Datenformat: 139 x 80 mm
1-teilig, gestanzt, genutet, einseitig geklebt geliefert
Bitte verwenden Sie für positive Schriftstärken mindestens 9pt (ca. 3,17mm) und bei negativen Schriftstärken mindestens 13pt (ca. 4,59mm).
Abmessungen / Druck- / Designvorlage, Logo, etc.: https://dateiwolke.example/ordner/X7KPtrWQ#m4vbeLhNcyrGzzt9_k2w8p

```html
<!DOCTYPE html>
<html lang="de">
<head>
<meta charset="utf-8">
<title>RuchKontor – Probenblister</title>
<link href="https://fonts.googleapis.com/css2?family=Josefin+Sans:wght@400&family=Dancing+Script:wght@400&family=Open+Sans:wght@400&display=swap" rel="stylesheet">
<style>
  :root {
    --page: #e4e4e4;
    --paper: #ffffff;
    --lilac: #6f58a8;
    --lilac-soft: #b7a8d8;
    --wash: #ece6f4;
    --wash-deep: #d9cfea;
    --leaf-grey: #c6cbdc;
  }
  * { margin: 0; padding: 0; box-sizing: border-box; }
  html, body { width: 1200px; height: 2330px; overflow: hidden; }
  body {
    background: var(--page);
    display: flex;
    flex-direction: column;
    justify-content: center;
    align-items: center;
    gap: 80px;
  }
  .spread {
    width: 1100px;
    height: 300px;
    display: flex;
    gap: 12px;
  }
  .panel {
    position: relative;
    flex: 1;
    background: var(--paper);
    overflow: hidden;
  }
  .wash {
    position: absolute;
    border-radius: 50%;
    background: radial-gradient(circle, var(--wash) 0%, rgba(236,230,244,0) 70%);
  }
  .dot {
    position: absolute;
    border-radius: 50%;
    background: var(--lilac-soft);
    opacity: .75;
  }
  .botanical {
    position: absolute;
  }
  .botanical--back-top {
    left: 0; top: 0; width: 260px; height: 90px;
    background: radial-gradient(ellipse at 20% 10%, var(--wash-deep) 0%, rgba(217,207,234,.4) 50%, rgba(255,255,255,0) 80%);
  }
  .botanical--back-bottom {
    left: 0; bottom: 0; width: 420px; height: 230px;
    background: radial-gradient(ellipse at 45% 85%, var(--leaf-grey) 0%, var(--wash-deep) 40%, rgba(236,230,244,0) 75%);
  }
  .botanical--inside {
    left: 0; top: 0; width: 140px; height: 300px;
    background: linear-gradient(90deg, var(--wash-deep) 0%, rgba(236,230,244,.5) 50%, rgba(255,255,255,0) 100%);
  }
  .stamp-field {
    position: absolute;
    left: 30px; bottom: 14px;
    width: 180px; height: 66px;
    background: var(--paper);
    border-radius: 10px;
  }
  .brand {
    position: absolute;
    display: flex;
    align-items: center;
    gap: 8px;
    font-family: "Josefin Sans", sans-serif;
    font-weight: 400;
    color: var(--lilac);
    white-space: nowrap;
  }
  .brand__mark {
    border-radius: 50%;
    background: var(--lilac);
  }
  .brand--small { left: 82px; top: 82px; font-size: 16px; }
  .brand--small .brand__mark { width: 10px; height: 10px; }
  .brand--large { right: 30px; top: 110px; font-size: 30px; }
  .brand--large .brand__mark { width: 22px; height: 22px; }
  .quote {
    position: absolute;
    left: 20px; top: 62px;
    width: 230px;
    text-align: center;
    font-family: "Dancing Script", cursive;
    font-size: 25px;
    line-height: 30px;
    color: var(--lilac);
  }
  .quote__source {
    display: block;
    margin-top: 12px;
    padding-left: 60px;
    font-family: "Open Sans", sans-serif;
    font-size: 11px;
    line-height: 14px;
  }
</style>
</head>
<body>

<section class="spread spread--outside" aria-label="Außenseite">
  <div class="panel panel--back">
    <div class="wash" style="left:120px;top:-60px;width:420px;height:220px"></div>
    <div class="botanical botanical--back-top" role="img" aria-label="Aquarell-Blüten in Lila"></div>
    <div class="botanical botanical--back-bottom" role="img" aria-label="Aquarell-Eukalyptusblätter und Zweige in Grau und Lila"></div>
    <div class="brand brand--small"><span class="brand__mark"></span>RuchKontor</div>
    <div class="stamp-field" aria-label="Feld für Stempel oder Aufkleber"></div>
    <span class="dot" style="left:478px;top:262px;width:16px;height:16px"></span>
    <span class="dot" style="left:490px;top:220px;width:8px;height:8px"></span>
  </div>
  <div class="panel panel--front">
    <div class="wash" style="left:-80px;top:80px;width:500px;height:260px"></div>
    <div class="brand brand--large"><span class="brand__mark"></span>RuchKontor</div>
    <span class="dot" style="left:480px;top:24px;width:30px;height:30px"></span>
    <span class="dot" style="left:452px;top:14px;width:22px;height:22px"></span>
    <span class="dot" style="left:310px;top:20px;width:14px;height:14px"></span>
    <span class="dot" style="left:300px;top:130px;width:20px;height:20px"></span>
    <span class="dot" style="left:440px;top:240px;width:24px;height:24px"></span>
    <span class="dot" style="left:120px;top:250px;width:10px;height:10px"></span>
  </div>
</section>

<section class="spread spread--inside" aria-label="Innenseite">
  <div class="panel panel--quote">
    <div class="wash" style="left:60px;top:-40px;width:480px;height:260px"></div>
    <div class="botanical botanical--inside" role="img" aria-label="Aquarell-Zweige und Blätter in Lila"></div>
    <p class="quote">„Düfte sind wie<br>die Seele der Blumen,<br>man kann sie fühlen,<br>selbst im Reich der<br>Schatten.“<span class="quote__source">Jonas Aubert</span></p>
    <span class="dot" style="left:210px;top:14px;width:16px;height:16px"></span>
    <span class="dot" style="left:380px;top:60px;width:12px;height:12px"></span>
    <span class="dot" style="left:320px;top:140px;width:18px;height:18px"></span>
    <span class="dot" style="left:180px;top:270px;width:14px;height:14px"></span>
  </div>
  <div class="panel panel--logo">
    <div class="wash" style="left:-60px;top:-30px;width:520px;height:300px"></div>
    <div class="brand brand--large" style="right:40px;top:108px;font-size:26px"><span class="brand__mark" style="width:18px;height:18px"></span>RuchKontor</div>
    <span class="dot" style="left:440px;top:20px;width:30px;height:30px"></span>
    <span class="dot" style="left:500px;top:14px;width:28px;height:28px"></span>
    <span class="dot" style="left:320px;top:40px;width:14px;height:14px"></span>
    <span class="dot" style="left:300px;top:150px;width:22px;height:22px"></span>
    <span class="dot" style="left:470px;top:260px;width:26px;height:26px"></span>
    <span class="dot" style="left:170px;top:280px;width:10px;height:10px"></span>
  </div>
</section>

</body>
</html>
```